Wix Website design for my therapy business - Willowmere Group

I have started designing a Wix site and have a good idea of what I want.
I have set up the pages, created some design ideas, and inputted the copy. I need someone fabulous to finish off the design aspects. I like working closely with the designers, I was an interior designer in an old career.
I would like the site to be funky but professional. My Wix skills are limited, and I just can't achieve the look I am wanting without having to spend a lot of time learning. If it's easier to start over, that's ok providing you use the same colours, font, images etc. I have included a screenshot of the home page below. I have another site I need to start as soon as we have finished this one.
I am looking for someone who is a good listener and is has design flare. I am easy to get along with and will respond quickly.
I would like to set up SEO and have help in the future.
Let me know if you are the right person for the job.
Target Market(s)
Please needing help with their mental health and for therapy.
Industry/Entity Type
Mental health
Font styles to use
Other font styles liked:
- Futura light
Requirements
Must have
- be easy to navigate and be simple yet stylish
Nice to have
- I have set up the basics of the site - nice to haves are already on the site
Should not have
- old fashioned large chunks of text.

```html
<!DOCTYPE html>
<html lang="en">
<head>
<meta charset="utf-8">
<title>Willowmere Group — Mental Health &amp; Therapy</title>
<link href="https://fonts.googleapis.com/css2?family=Jost:wght@300;400;500;600&family=Roboto:wght@300;400;500;700&display=swap" rel="stylesheet">
<style>
:root{
  --navy:#0b1733;
  --ink:#1d1d1f;
  --text:#6b6b6b;
  --accent:#9c7c5c;
  --accent-soft:#f1ebe4;
  --cream:#f3f1ec;
  --white:#ffffff;
  --line:#d9d4cc;
  --star:#f2b01e;
}
*{box-sizing:border-box;margin:0;padding:0}
html,body{width:1200px;height:3873px;overflow:hidden}
body{font-family:"Roboto",sans-serif;color:var(--ink);background:var(--white);position:relative}
.page{position:relative;width:1200px;height:3873px;overflow:hidden}
.abs{position:absolute}
.heading{font-family:"Jost",sans-serif;font-weight:600;color:var(--navy)}
.brand{font-family:"Jost",sans-serif;font-weight:400;color:var(--accent);letter-spacing:.5px}
.btn{display:flex;align-items:center;justify-content:center;border-radius:40px;background:var(--navy);color:var(--white);font-weight:500;font-size:13px;text-decoration:none}

.topbar{top:0;left:0;width:1200px;height:29px;background:var(--navy);color:var(--white);font-size:11.5px;display:flex;align-items:center;padding-left:113px;gap:40px}
.topbar span{display:flex;align-items:center;gap:10px}
.nav{top:29px;left:0;width:1200px;height:61px;background:var(--white)}
.nav .logo{left:113px;top:14px;font-size:30px}
.nav ul{list-style:none;display:flex;gap:22px;position:absolute;left:374px;top:24px;font-size:11.5px;font-weight:500;color:var(--ink)}
.nav .btn{left:934px;top:15px;width:153px;height:33px;font-size:11.5px}

.hero{top:90px;left:0;width:1200px;height:545px;background:linear-gradient(100deg,#a5896c 0%,#b39a80 35%,#8a7560 60%,#35584a 80%,#4f6a4a 100%);overflow:hidden}
.hero h1{left:112px;top:142px;font-family:"Jost",sans-serif;font-weight:600;font-size:50px;line-height:56px;color:var(--white);letter-spacing:.5px}
.hero p{left:112px;top:280px;width:430px;font-size:11.5px;line-height:18px;color:var(--white)}
.hero .btn{left:113px;top:366px;width:170px;height:38px;background:var(--white);color:var(--accent);font-size:12.5px}

.eyebrow{font-size:10.5px;color:var(--accent);text-align:center;width:100%}
.title{font-size:31px;text-align:center;width:100%}
.divider{display:flex;align-items:center;justify-content:center;gap:12px;width:100%}
.divider i{display:block;width:56px;height:1px;background:var(--accent);opacity:.6}
.divider b{font-family:"Jost",sans-serif;font-weight:400;color:var(--accent);font-size:15px}

.about-img{left:113px;top:687px;width:477px;height:385px;border-radius:8px;background:linear-gradient(135deg,#e8eef0 0%,#d7cfc6 50%,#b8a28e 100%);overflow:hidden}
.about .eyebrow{text-align:left}
.about-text{left:632px;top:706px;width:446px}
.about-text h2{font-size:30px;margin-top:12px}
.about-text .divider{justify-content:flex-start;margin-top:10px}
.about-text p{font-size:11px;line-height:18.8px;color:var(--text);margin-top:16px}
.about-text p+p{margin-top:0}
.about-text .btn{width:131px;height:37px;margin-top:24px}

.services{top:1128px;left:0;width:1200px;height:579px;background:linear-gradient(180deg,#ffffff 0%,#eaf2f5 18%,#bfe0e7 45%,#7cc5d2 70%,#9fd3da 100%)}
.svc-card{top:134px;width:307px;height:389px;background:var(--white);border-radius:6px;overflow:hidden;text-align:center;box-shadow:0 4px 14px rgba(0,0,0,.06)}
.svc-card .ph{width:100%;height:185px}
.svc-card h3{font-size:15.5px;font-weight:500;margin-top:33px;color:var(--ink)}
.svc-card p{font-size:11px;line-height:18.5px;color:var(--text);width:240px;margin:14px auto 0}
.svc-card .btn{position:absolute;left:88px;top:318px;width:131px;height:38px}
.arrow{width:38px;height:38px;border-radius:50%;background:var(--white);display:flex;align-items:center;justify-content:center;box-shadow:0 2px 8px rgba(0,0,0,.15)}

.why-card{top:1862px;width:272px;height:221px;background:var(--white);border-radius:6px;box-shadow:0 3px 16px rgba(0,0,0,.07);text-align:center}
.why-card .icon{width:72px;height:72px;border-radius:50%;background:var(--accent-soft);margin:24px auto 0;display:flex;align-items:center;justify-content:center}
.why-card h3{font-size:15.5px;font-weight:500;margin-top:20px}
.why-card p{font-size:11px;line-height:18.8px;color:var(--text);width:200px;margin:12px auto 0}

.appt{top:2136px;left:0;width:1200px;height:552px;background:linear-gradient(180deg,#c9d3d4 0%,#a9b0a2 35%,#b7a371 60%,#8b7a4c 100%);overflow:hidden}
.form-card{left:113px;top:37px;width:374px;height:468px;background:var(--white);border-radius:6px}
.form-card .eyebrow{position:absolute;top:30px}
.form-card h2{position:absolute;top:52px;font-size:22px;text-align:center;width:100%}
.form-card .divider{position:absolute;top:92px}
.field{position:absolute;left:23px;width:329px;height:36px;border:1px solid var(--line);border-radius:5px;font-size:10px;color:#8a8a8a;padding:12px 17px}
.form-card .btn{position:absolute;left:23px;top:394px;width:329px;height:39px}

.t-card{top:2862px;width:426px;height:229px;background:var(--white);border-radius:6px;box-shadow:0 3px 16px rgba(0,0,0,.07);text-align:center}
.avatar{position:absolute;left:180px;top:-27px;width:66px;height:66px;border-radius:50%;background:linear-gradient(160deg,#8f7a6a,#3e3a38);border:3px solid var(--white)}
.t-card h4{font-size:14px;font-weight:500;margin-top:58px}
.t-card .role{font-size:10px;color:var(--text);margin-top:6px}
.stars{display:flex;justify-content:center;gap:3px;margin-top:8px}
.t-card p{font-size:10.5px;line-height:19px;color:var(--text);width:346px;margin:24px auto 0}
.q{position:absolute;font-family:"Jost",sans-serif;font-size:40px;color:#d6d6d6;line-height:1}

.blog{top:3139px;left:0;width:1200px;height:535px;background:var(--cream)}
.b-card{top:152px;width:283px;height:340px;background:var(--white);overflow:hidden}
.b-card .ph{height:177px}
.b-card .date{font-size:11px;color:var(--accent);margin:24px 0 0 25px}
.b-card h3{font-size:14.5px;font-weight:600;line-height:22px;color:var(--navy);margin:14px 25px 0;height:44px}
.b-card a{display:flex;align-items:center;gap:8px;font-size:11.5px;font-weight:500;color:var(--navy);text-decoration:none;margin:14px 0 0 25px}

.footer{top:3674px;left:0;width:1200px;height:199px;background:var(--navy);color:var(--white)}
.footer .logo{left:113px;top:22px;font-size:28px;color:var(--white)}
.socials{left:113px;top:80px;display:flex;gap:7px}
.socials i{display:block;width:20px;height:20px;border:1.5px solid var(--white);border-radius:50%}
.copy{left:113px;top:128px;font-size:10px}
.fcol h5{font-size:13.5px;font-weight:500;margin-bottom:14px}
.fcol li{list-style:none;font-size:10px;line-height:19px}
.contact li{display:flex;gap:12px;align-items:flex-start;line-height:15px;margin-bottom:9px}
.news h5{font-size:17px;font-weight:500}
.news .box{display:flex;margin-top:14px}
.news .box span{width:132px;height:35px;border:1px solid var(--white);font-size:9px;padding:12px 10px;color:#c8ccd6}
.news .box b{width:102px;height:35px;background:var(--white);color:var(--navy);font-size:11px;font-weight:500;display:flex;align-items:center;justify-content:center}
</style>
</head>
<body>
<div class="page">

  <div class="topbar abs">
    <span><svg width="12" height="12" viewBox="0 0 24 24" fill="#fff"><path d="M6.6 10.8a15.1 15.1 0 0 0 6.6 6.6l2.2-2.2a1 1 0 0 1 1-.25 11.4 11.4 0 0 0 3.6.57 1 1 0 0 1 1 1V20a1 1 0 0 1-1 1A17 17 0 0 1 3 4a1 1 0 0 1 1-1h3.5a1 1 0 0 1 1 1c0 1.25.2 2.45.57 3.57a1 1 0 0 1-.25 1z"/></svg>(02) 4711 2090</span>
    <span style="margin-left:40px"><svg width="13" height="10" viewBox="0 0 26 20" fill="none" stroke="#fff" stroke-width="2"><rect x="1" y="1" width="24" height="18"/><path d="M1 1l12 10L25 1"/></svg>info@willowmeregroup.com.au</span>
  </div>

  <header class="nav abs">
    <div class="logo brand abs">Willowmere</div>
    <ul>
      <li>Home</li><li>About Us</li><li>Therapy Type</li><li>Addictions</li><li>Program List</li><li>Resources</li><li>Blog</li><li>Contact</li>
    </ul>
    <a class="btn abs">Schedule Appointment</a>
  </header>

  <section class="hero abs" role="img" aria-label="Smiling woman with curly hair in a green top, leafy plants behind her">
    <h1 class="abs">Welcome To The<br>Willowmere Group</h1>
    <p class="abs">Mental health refers to a person's emotional, psychological, and social well-being. It affects how people think, feel, and act, and it also influences how they handle stress, relate to others, and make choices.</p>
    <a class="btn abs">Request a Consultation</a>
  </section>

  <section class="about">
    <div class="about-img abs" role="img" aria-label="Therapist with clipboard meeting a young couple seated on a sofa"></div>
    <div class="about-text abs">
      <div class="eyebrow">About The Willowmere Group</div>
      <h2 class="heading">Providing Excellent Care</h2>
      <div class="divider"><i></i><b>Willowmere</b><i></i></div>
      <p>Maintaining good mental health is crucial for overall well-being and can contribute to improved physical health, productivity, and quality of life. Mental health issues can arise from a variety of factors, including biological factors (such as genetics or brain chemistry), life experiences (such as trauma or abuse), and family history of mental health problems.</p>
      <p>Common mental health disorders include anxiety disorders, depression, bipolar disorder, schizophrenia, and eating disorders. Symptoms of mental health disorders can vary widely but may include changes in mood, behavior, thoughts, and feelings. It's important to note that mental health disorders are treatable, and with the right support, many people can recover and lead fulfilling lives.</p>
      <a class="btn">Read More</a>
    </div>
  </section>

  <section class="services abs" role="img" aria-label="Calm turquoise sea under a pale sky">
    <div class="eyebrow abs" style="top:19px">Our Services</div>
    <h2 class="title heading abs" style="top:38px">How We Can</h2>
    <div class="divider abs" style="top:89px"><i></i><b>Willowmere</b><i></i></div>

    <div class="svc-card abs" style="left:113px">
      <div class="ph" role="img" aria-label="Clinician fitting an EEG cap on a seated patient" style="background:linear-gradient(135deg,#dfe6ec,#a9b8c9 60%,#c9a98a)"></div>
      <h3>Neurofeedback Therapy</h3>
      <p>Neurofeedback is a gentle and safe treatment that harnesses the potential of neuroplasticity for healing and growth.</p>
      <a class="btn">Read More</a>
    </div>
    <div class="svc-card abs" style="left:447px">
      <div class="ph" role="img" aria-label="Close-up of an eye" style="background:linear-gradient(160deg,#e2c4b1,#c99e86 55%,#b48a72)"></div>
      <h3>EMDR</h3>
      <p>EMDR is a targeted therapy that helps alleviate the distress associated with traumatic memories.</p>
      <a class="btn">Read More</a>
    </div>
    <div class="svc-card abs" style="left:779px">
      <div class="ph" role="img" aria-label="Group meditating on mats in a bright studio" style="background:linear-gradient(135deg,#c9ccc8,#8e8f8a 55%,#5e625c)"></div>
      <h3>Mindfulness Training</h3>
      <p>Mindfulness is the conscious awareness of present moment awareness that supports the maintenance of our emotional well-being.</p>
      <a class="btn">Read More</a>
    </div>

    <div class="arrow abs" style="left:34px;top:279px"><svg width="12" height="12" viewBox="0 0 12 12"><path d="M8 1L3 6l5 5" fill="none" stroke="#111" stroke-width="1.6"/></svg></div>
    <div class="arrow abs" style="left:1121px;top:279px"><svg width="12" height="12" viewBox="0 0 12 12"><path d="M4 1l5 5-5 5" fill="none" stroke="#111" stroke-width="1.6"/></svg></div>
  </section>

  <section class="why">
    <div class="eyebrow abs" style="top:1749px">Advantages</div>
    <h2 class="title heading abs" style="top:1766px">Why Choose Us</h2>
    <div class="divider abs" style="top:1817px"><i></i><b>Willowmere</b><i></i></div>

    <div class="why-card abs" style="left:173px">
      <div class="icon"><svg width="34" height="34" viewBox="0 0 34 34" fill="none" stroke="#9c7c5c" stroke-width="1.4"><path d="M17 26c-4-3-6-7-6-11 2 1 4 3 6 6 2-3 4-5 6-6 0 4-2 8-6 11z"/><path d="M17 21c-1-4 0-8 0-12 1 4 1 8 0 12"/><path d="M11 15c-3 0-5 2-6 5 3 1 7 2 12 6"/><path d="M23 15c3 0 5 2 6 5-3 1-7 2-12 6"/></svg></div>
      <h3>Evidence Based</h3>
      <p>Our experts utilize evidence-based assessment tools that objectively measure functioning.</p>
    </div>
    <div class="why-card abs" style="left:463px">
      <div class="icon"><svg width="34" height="34" viewBox="0 0 34 34" fill="none" stroke="#9c7c5c" stroke-width="1.4"><path d="M12 28v-5c-3-2-5-5-5-9a10 10 0 0 1 20 0l3 5h-3v4h-4v5"/><path d="M15 10h5v5h-5zM13 17h4"/></svg></div>
      <h3>Tailored Services</h3>
      <p>We provide services that are tailored to meet the specific needs of each individual patient.</p>
    </div>
    <div class="why-card abs" style="left:754px">
      <div class="icon"><svg width="34" height="34" viewBox="0 0 34 34" fill="none" stroke="#9c7c5c" stroke-width="1.4"><path d="M12 28v-5c-3-2-5-5-5-9a10 10 0 0 1 20 0l3 5h-3v4h-4v5"/><circle cx="17" cy="13" r="4"/><circle cx="17" cy="13" r="1.5"/></svg></div>
      <h3>Vast Experience</h3>
      <p style="margin-top:16px">Our doctors are experts in the fields of pediatric and adult neuropsychology.</p>
    </div>
  </section>

  <section class="appt abs" role="img" aria-label="Woman meditating with eyes closed among tall wild grasses beside a lake and hills">
    <form class="form-card abs">
      <div class="eyebrow">Have questions?</div>
      <h2 class="heading">Schedule an Appointment!</h2>
      <div class="divider"><i></i><b>Willowmere</b><i></i></div>
      <div class="field" style="top:139px">Your Name</div>
      <div class="field" style="top:187px">Phone Number</div>
      <div class="field" style="top:235px">Email</div>
      <div class="field" style="top:283px;height:92px">Message</div>
      <a class="btn">Submit</a>
    </form>
  </section>

  <section class="testimonials">
    <div class="eyebrow abs" style="top:2725px">Testimonials</div>
    <h2 class="title heading abs" style="top:2742px">What Our Client Says</h2>
    <div class="divider abs" style="top:2793px"><i></i><b>Willowmere</b><i></i></div>

    <div class="t-card abs" style="left:152px">
      <div class="avatar" role="img" aria-label="Portrait of a male client"></div>
      <h4>Marcel D.</h4>
      <div class="role">Industry Specialist</div>
      <div class="stars"><svg width="80" height="13" viewBox="0 0 80 13" fill="#f2b01e"><g id="s"><path d="M6.5 0l1.9 4.2 4.6.4-3.5 3 1.1 4.5-4.1-2.4-4 2.4 1-4.5L0 4.6l4.6-.4z"/></g><use href="#s" x="16.5"/><use href="#s" x="33"/><use href="#s" x="49.5"/><use href="#s" x="66"/></svg></div>
      <span class="q" style="left:24px;top:110px">“</span>
      <p>I had a great experience with Birchline Roofing from start to finish. They took the time to explain in details what was wrong with my roof and gave me a very competitive estimate.</p>
      <span class="q" style="left:272px;top:187px">”</span>
    </div>
    <div class="t-card abs" style="left:621px">
      <div class="avatar" role="img" aria-label="Portrait of a female client"></div>
      <h4>Lena P.</h4>
      <div class="role">Specialist</div>
      <div class="stars"><svg width="80" height="13" viewBox="0 0 80 13" fill="#f2b01e"><use href="#s"/><use href="#s" x="16.5"/><use href="#s" x="33"/><use href="#s" x="49.5"/><use href="#s" x="66"/></svg></div>
      <span class="q" style="left:42px;top:110px">“</span>
      <p style="width:320px">I have been using Birchline Roofing over 10-15 years. They have put new roofs on 2 homes that I have owned and also siding on my family room this past year.</p>
      <span class="q" style="left:253px;top:187px">”</span>
    </div>
  </section>

  <section class="blog abs">
    <div class="eyebrow abs" style="top:37px">News &amp; Blog</div>
    <h2 class="title heading abs" style="top:55px">Our Latest Blog</h2>
    <div class="divider abs" style="top:106px"><i></i><b>Willowmere</b><i></i></div>

    <article class="b-card abs" style="left:137px">
      <div class="ph" role="img" aria-label="Woman in a face mask reading at a train station" style="background:linear-gradient(135deg,#c79b6e,#9e6a45 50%,#4f4a46)"></div>
      <div class="date">May 16 2023</div>
      <h3>Do You Actually Need A Personal Trainer?</h3>
      <a>Read More <svg width="13" height="10" viewBox="0 0 13 10" fill="none" stroke="#0b1733" stroke-width="1.4"><path d="M0 5h12M8 1l4 4-4 4"/></svg></a>
    </article>
    <article class="b-card abs" style="left:462px">
      <div class="ph" role="img" aria-label="Masked medical staff talking in a bright clinic corridor" style="background:linear-gradient(135deg,#d8e3ea,#9fb6c8 55%,#5d7488)"></div>
      <div class="date">April 12 2023</div>
      <h3>Understanding The Different Types Of Braces</h3>
      <a>Read More <svg width="13" height="10" viewBox="0 0 13 10" fill="none" stroke="#0b1733" stroke-width="1.4"><path d="M0 5h12M8 1l4 4-4 4"/></svg></a>
    </article>
    <article class="b-card abs" style="left:782px">
      <div class="ph" role="img" aria-label="Doctors in discussion around a laptop in an office" style="background:linear-gradient(135deg,#d9d2c7,#a89d8f 55%,#4e5d70)"></div>
      <div class="date">December 19 2022</div>
      <h3>How To Choose The Right Pillow For Good Posture</h3>
      <a>Read More <svg width="13" height="10" viewBox="0 0 13 10" fill="none" stroke="#0b1733" stroke-width="1.4"><path d="M0 5h12M8 1l4 4-4 4"/></svg></a>
    </article>
  </section>

  <footer class="footer abs">
    <div class="logo brand abs">Willowmere</div>
    <div class="socials abs"><i></i><i></i><i></i><i></i></div>
    <div class="copy abs">© 2023 Willowmere Group</div>

    <div class="fcol abs" style="left:283px;top:38px">
      <h5>About</h5>
      <ul><li>Patient Portal</li><li>Billing &amp; Financial Services</li><li>Medical Records</li><li>All Patient Tools</li></ul>
    </div>
    <div class="fcol abs" style="left:445px;top:38px">
      <h5>Patient Tools</h5>
      <ul><li>Patient Portal</li><li>Billing &amp; Financial Services</li><li>Medical Records</li><li>All Patient Tools</li></ul>
    </div>
    <div class="fcol contact abs" style="left:611px;top:38px">
      <h5>Contact Us</h5>
      <ul>
        <li><svg width="11" height="11" viewBox="0 0 24 24" fill="#fff"><path d="M6.6 10.8a15.1 15.1 0 0 0 6.6 6.6l2.2-2.2a1 1 0 0 1 1-.25 11.4 11.4 0 0 0 3.6.57 1 1 0 0 1 1 1V20a1 1 0 0 1-1 1A17 17 0 0 1 3 4a1 1 0 0 1 1-1h3.5a1 1 0 0 1 1 1c0 1.25.2 2.45.57 3.57a1 1 0 0 1-.25 1z"/></svg>(866) 555-0142</li>
        <li><svg width="11" height="9" viewBox="0 0 26 20" fill="#fff"><rect x="1" y="1" width="24" height="18"/></svg>info@willowmeregroup.com.au</li>
        <li><svg width="11" height="13" viewBox="0 0 20 26" fill="#fff"><path d="M10 0a9 9 0 0 1 9 9c0 7-9 17-9 17S1 16 1 9a9 9 0 0 1 9-9zm0 5a4 4 0 1 0 0 8 4 4 0 0 0 0-8z"/></svg>4F 210 Harbour Street, Fernleigh<br>Business Centre, Alder Bay 2031</li>
      </ul>
    </div>
    <div class="news abs" style="left:826px;top:36px">
      <h5>Subscribe To Our Newsletter</h5>
      <div class="box"><span>Enter your email</span><b>Subscribe Now</b></div>
    </div>
  </footer>

</div>
</body>
</html>
```